Birchwood Claims Services
Property Claims Management, Catastrophe Services
Birchwood Claims Services -
Creative Brief
Professional
Tom Fenwick
President
4817 Copper Mill Lane Dunmore Township, PA 18519
tom@birchwoodclaimservices.example
birchwoodclaimservices.example

```html
<!DOCTYPE html>
<html lang="en">
<head>
<meta charset="utf-8">
<title>Birchwood Claims Services – Stationery</title>
<link rel="stylesheet" href="https://fonts.googleapis.com/css2?family=Cinzel:wght@700&family=Open+Sans:wght@400;600&display=swap">
<style>
  :root {
    --ground: #e9e4dc;
    --paper: #ffffff;
    --green: #1f8a3c;
    --green-dark: #0f6a2a;
    --green-faint: #e8f2ea;
    --ink: #4a4a4a;
    --ink-soft: #8a8a8a;
    --edge: #d6d2cb;
  }
  * { box-sizing: border-box; margin: 0; padding: 0; }
  html, body { width: 1200px; height: 446px; overflow: hidden; }
  body { background: var(--ground); font-family: "Open Sans", sans-serif; color: var(--ink); position: relative; }

  .sheet { position: absolute; background: var(--paper); box-shadow: 0 2px 6px rgba(0,0,0,.18); overflow: hidden; }

  .brand { display: flex; align-items: center; gap: 5px; }
  .brand-dot { border-radius: 50%; background: var(--green); flex: none; }
  .brand-name { font-family: "Cinzel", serif; font-weight: 700; color: var(--green); line-height: 1.05; text-transform: uppercase; }

  .tiny { font-size: 4px; line-height: 1.5; color: var(--ink-soft); white-space: nowrap; }

  .decor-ring { position: absolute; border-radius: 50%; border: 14px solid var(--green-faint); }

  /* presentation logo */
  .master-logo { position: absolute; left: 24px; top: 94px; }
  .master-logo .brand-dot { width: 30px; height: 30px; }
  .master-logo .brand-name { font-size: 14px; width: 150px; }
  .master-logo .caption { font-size: 8px; color: var(--ink); margin: 6px 0 0 35px; }

  /* business cards */
  .card { left: 29px; width: 182px; height: 92px; padding: 9px 10px; }
  .card-front { top: 250px; }
  .card-back { top: 352px; }
  .card .brand-dot { width: 10px; height: 10px; }
  .card .brand-name { font-size: 6px; width: 80px; }
  .card-body { display: flex; justify-content: space-between; margin-top: 14px; }
  .card-person { text-align: right; }
  .card-person .name { font-size: 6px; font-weight: 600; color: var(--green); }
  .card-person .role { font-size: 4px; color: var(--ink-soft); }
  .card-web { position: absolute; bottom: 5px; left: 0; right: 0; text-align: center; font-size: 4px; color: var(--green); }

  /* letterheads */
  .letterhead { top: 29px; width: 276px; height: 384px; padding: 14px 16px; }
  .letterhead-first { left: 233px; }
  .letterhead-second { left: 533px; }
  .letterhead-top { display: flex; justify-content: space-between; align-items: flex-start; }
  .letterhead .brand-dot { width: 16px; height: 16px; }
  .letterhead .brand-name { font-size: 8px; width: 110px; }
  .letterhead .decor-ring { width: 130px; height: 130px; left: 50%; top: 50%; transform: translate(-50%,-60%); }
  .letterhead-foot { position: absolute; bottom: 12px; left: 0; right: 0; text-align: center; }
  .letterhead-second .letterhead-top { justify-content: center; }

  /* envelopes */
  .envelope { left: 833px; width: 343px; }
  .envelope-back { top: 29px; height: 139px; }
  .envelope-back .flap { position: absolute; inset: 0; }
  .envelope-back .brand { position: absolute; left: 50%; top: 16px; transform: translateX(-50%); }
  .envelope-back .brand-dot { width: 12px; height: 12px; background: var(--paper); }
  .envelope-back .brand-name { font-size: 7px; color: var(--paper); width: 90px; }

  .envelope-front { top: 185px; height: 139px; }
  .envelope-front .flap { position: absolute; inset: 0; }
  .envelope-front .brand { position: absolute; left: 50%; top: 22px; transform: translateX(-50%); }
  .envelope-front .brand-dot { width: 10px; height: 10px; }
  .envelope-front .brand-name { font-size: 6px; width: 80px; }
  .envelope-front .return { position: absolute; bottom: 4px; left: 0; right: 0; text-align: center; }

  .envelope-window { top: 336px; height: 96px; padding: 12px 14px; }
  .envelope-window .brand-dot { width: 12px; height: 12px; }
  .envelope-window .brand-name { font-size: 7px; width: 90px; }
  .envelope-window .tiny { margin: 3px 0 0 17px; }
  .envelope-window .decor-ring { width: 80px; height: 80px; right: 20px; top: 8px; border-width: 9px; }
</style>
</head>
<body>

<div class="master-logo">
  <div class="brand">
    <span class="brand-dot"></span>
    <span class="brand-name">Birchwood Claims Services</span>
  </div>
  <p class="caption">Property Claims Management</p>
</div>

<section class="sheet card card-front">
  <div class="brand"><span class="brand-dot"></span><span class="brand-name">Birchwood Claims Services</span></div>
  <div class="card-body">
    <div class="tiny">4817 Copper Mill Lane<br>Dunmore Township, PA 18519<br>T 570 555 0143<br>tom@birchwoodclaimservices.example</div>
    <div class="card-person"><p class="name">Tom Fenwick</p><p class="role">President</p></div>
  </div>
  <p class="card-web">birchwoodclaimservices.example</p>
</section>

<section class="sheet card card-back">
  <div class="brand"><span class="brand-dot"></span><span class="brand-name">Birchwood Claims Services</span></div>
  <div class="card-body">
    <div class="tiny">4817 Copper Mill Lane<br>Dunmore Township, PA 18519<br>F 570 555 0144<br>tom@birchwoodclaimservices.example</div>
    <div class="card-person"><p class="name">Tom Fenwick</p><p class="role">President</p></div>
  </div>
  <p class="card-web">birchwoodclaimservices.example</p>
</section>

<section class="sheet letterhead letterhead-first">
  <div class="letterhead-top">
    <div class="brand"><span class="brand-dot"></span><span class="brand-name">Birchwood Claims Services</span></div>
    <div class="tiny">4817 Copper Mill Lane<br>Dunmore Township, PA 18519<br>T 570 555 0143<br>tom@birchwoodclaimservices.example<br>birchwoodclaimservices.example</div>
  </div>
  <span class="decor-ring"></span>
  <p class="letterhead-foot tiny">birchwoodclaimservices.example</p>
</section>

<section class="sheet letterhead letterhead-second">
  <div class="letterhead-top">
    <div class="brand"><span class="brand-dot"></span><span class="brand-name">Birchwood Claims Services</span></div>
  </div>
  <span class="decor-ring"></span>
  <div class="letterhead-foot tiny">4817 Copper Mill Lane Dunmore Township, PA 18519 · T 570 555 0143<br>birchwoodclaimservices.example</div>
</section>

<section class="sheet envelope envelope-back">
  <svg class="flap" viewBox="0 0 343 139" preserveAspectRatio="none" aria-hidden="true">
    <polygon points="0,0 343,0 343,40 171.5,90 0,40" fill="var(--green)"/>
    <polyline points="0,40 171.5,90 343,40" fill="none" stroke="var(--green-dark)" stroke-width="1"/>
  </svg>
  <div class="brand"><span class="brand-dot"></span><span class="brand-name">Birchwood Claims Services</span></div>
</section>

<section class="sheet envelope envelope-front">
  <svg class="flap" viewBox="0 0 343 139" preserveAspectRatio="none" aria-hidden="true">
    <polyline points="0,0 171.5,80 343,0" fill="none" stroke="var(--edge)" stroke-width="1"/>
    <polyline points="0,139 130,70" fill="none" stroke="var(--edge)" stroke-width="1"/>
    <polyline points="343,139 213,70" fill="none" stroke="var(--edge)" stroke-width="1"/>
  </svg>
  <div class="brand"><span class="brand-dot"></span><span class="brand-name">Birchwood Claims Services</span></div>
  <p class="return tiny">birchwoodclaimservices.example</p>
</section>

<section class="sheet envelope envelope-window">
  <div class="brand"><span class="brand-dot"></span><span class="brand-name">Birchwood Claims Services</span></div>
  <p class="tiny">4817 Copper Mill Lane<br>Dunmore Township, PA 18519</p>
  <span class="decor-ring"></span>
</section>

</body>
</html>
```